Organic Mavu (Coffee) Scrub Label for high end product

Need a product label for a coffee based body scrub called Mavu Body Scrub a 100% organic product. Our primary target is the yoga community so designs should reflect calm, perhaps incorporate eastern yoga symbology. simpler the better. Design should include both a round lid label and a rectangular wrap around label.

Target Market(s)

yoga community, people with cellulite, etc.

Industry/Entity Type

Community

```html
<!DOCTYPE html>
<html lang="en">
<head>
<meta charset="utf-8">
<title>Mavu Body Scrub – Label Presentation</title>
<link rel="stylesheet" href="https://fonts.googleapis.com/css2?family=Josefin+Sans:wght@400;600&display=swap">
<style>
  :root {
    --board-white: #ffffff;
    --board-grey: #e6e7e8;
    --label-tan: #c49a6c;
    --label-tan-soft: #ecdcc9;
    --label-white: #ffffff;
    --ink: #111111;
    --type: "Josefin Sans", Arial, sans-serif;
  }
  * { margin: 0; padding: 0; box-sizing: border-box; }
  html, body { width: 1200px; height: 848px; overflow: hidden; }
  body { font-family: var(--type); color: var(--ink); }

  .board { position: relative; width: 1200px; height: 848px; background: var(--board-white); }
  .board__panel-right {
    position: absolute; left: 600px; top: 0; width: 600px; height: 848px;
    background: var(--board-grey);
  }

  .mark-equation {
    position: absolute; left: 104px; top: 108px; height: 50px;
    display: flex; align-items: center; gap: 28px;
  }
  .mark-equation__part { background: var(--ink); border-radius: 4px; height: 40px; }
  .mark-equation__part--lotus { width: 84px; }
  .mark-equation__part--bean { width: 18px; border-radius: 9px; }
  .mark-equation__part--result { width: 90px; }
  .mark-equation__operator { font-size: 46px; font-weight: 600; line-height: 1; }

  .lid-label { position: absolute; left: 762px; top: 44px; width: 286px; height: 286px; }
  .wrap-label { position: absolute; left: 683px; top: 376px; width: 443px; height: 405px; }

  svg text { font-family: var(--type); }
</style>
</head>
<body>
<main class="board">
  <div class="board__panel-right"></div>

  <div class="mark-equation">
    <div class="mark-equation__part mark-equation__part--lotus" role="img" aria-label="Lotus symbol"></div>
    <span class="mark-equation__operator">+</span>
    <div class="mark-equation__part mark-equation__part--bean" role="img" aria-label="Coffee bean symbol"></div>
    <span class="mark-equation__operator">=</span>
    <div class="mark-equation__part mark-equation__part--result" role="img" aria-label="Combined lotus and coffee bean mark"></div>
  </div>

  <svg class="lid-label" viewBox="0 0 286 286" aria-label="Round lid label">
    <circle cx="143" cy="143" r="143" fill="var(--label-white)"/>
    <rect class="lid-label__ornament" x="86" y="30" width="114" height="14" rx="7" fill="var(--label-tan-soft)" role="img" aria-label="Dotted arc ornament"/>
    <text class="lid-label__name" x="143" y="141" text-anchor="middle" font-size="70" font-weight="600" fill="var(--ink)">Mavu</text>
    <text class="lid-label__product" x="143" y="177" text-anchor="middle" font-size="20" font-weight="600" letter-spacing="1" fill="var(--label-tan)">BODY SCRUB</text>
    <circle class="lid-label__mark" cx="143" cy="212" r="8" fill="var(--ink)"/>
    <path d="M 50 196 Q 143 292 236 196" fill="none" stroke="var(--label-tan)" stroke-width="20"/>
    <path id="lid-arc-text" d="M 50 200 Q 143 296 236 200" fill="none"/>
    <text font-size="11" font-weight="600" letter-spacing="1.6" fill="var(--label-white)">
      <textPath href="#lid-arc-text" startOffset="50%" text-anchor="middle">100% NATURAL PRODUCT</textPath>
    </text>
  </svg>

  <svg class="wrap-label" viewBox="0 0 443 405" aria-label="Rectangular wrap label">
    <rect width="443" height="405" fill="var(--label-tan)" role="img" aria-label="Fine diamond lattice pattern on tan"/>
    <rect y="164" width="443" height="110" fill="var(--label-white)"/>
    <circle cx="222" cy="216" r="113" fill="var(--label-white)"/>
    <rect class="wrap-label__ornament" x="176" y="102" width="92" height="14" rx="7" fill="var(--label-tan-soft)" role="img" aria-label="Dotted arc ornament"/>
    <text x="222" y="212" text-anchor="middle" font-size="68" font-weight="600" fill="var(--ink)">Mavu</text>
    <text x="222" y="258" text-anchor="middle" font-size="20" font-weight="600" letter-spacing="1" fill="var(--label-tan)">BODY SCRUB</text>
    <circle class="wrap-label__mark" cx="222" cy="288" r="8" fill="var(--ink)"/>
    <g font-size="11.5" font-weight="600" letter-spacing="1.8" fill="var(--ink)" text-anchor="middle">
      <text x="57" y="196">ORGANIC</text>
      <text x="57" y="213">COFFEE</text>
      <text x="57" y="230">SCRUB</text>
      <text x="393" y="191">100%</text>
      <text x="393" y="208">NATURAL</text>
      <text x="393" y="225">PRODUCT</text>
    </g>
  </svg>
</main>
</body>
</html>
```